"Leibeswerkstatt" private practice for physiotherapy

we are looking for a flyer design for a private practice for physiotherapy. the name of the practice is "Leibeswerkstatt".
Treatments such as: manual therapy, manual lymphatic drainage, classic massage, sectoral alternative practitioners are offered

The flyers should be double-sided and the format DIN long (105x210 mm)

Font styles to use
Serif

Colors
0094D4
00A9DD
6FCCEA
C7EBF8
E9F6FB

Requirements
Must have
• Leibeswerkstatt, Lindenweg 17, 07391 Beispielort / Leibeswerkstatt-beispielort.de / Tel. 03581 7140258

```html
<!DOCTYPE html>
<html lang="de">
<head>
<meta charset="utf-8">
<title>Leibeswerkstatt – Flyer</title>
<link rel="stylesheet" href="https://fonts.googleapis.com/css2?family=Josefin+Sans:wght@600;700&family=Barlow+Condensed:ital,wght@0,400;0,500;1,300&display=swap">
<style>
  :root{
    --navy:#3a4656;
    --sky:#89b5d9;
    --paper:#ffffff;
    --page:#ffffff;
    --text-dark:#2f3540;
  }
  *{margin:0;padding:0;box-sizing:border-box}
  html,body{width:1200px;height:960px;overflow:hidden;background:var(--page)}
  .canvas{position:relative;width:1200px;height:960px}
  .flyer{position:absolute;top:98px;width:382px;height:764px;background:var(--paper);overflow:hidden;box-shadow:0 2px 10px rgba(0,0,0,.12)}
  .flyer--front{left:201px}
  .flyer--back{left:634px}

  .front-art{position:absolute;left:0;top:0}
  .tagline{position:absolute;left:0;width:100%;text-align:center}
  .tagline__lead{top:44px;font:italic 300 38px/1 "Barlow Condensed",sans-serif;color:var(--sky)}
  .tagline__main{top:92px;font:700 36px/1 "Josefin Sans",sans-serif;letter-spacing:2.5px;color:var(--text-dark)}
  .brand-name{position:absolute;font:700 29px/1 "Josefin Sans",sans-serif;color:var(--text-dark);letter-spacing:.5px}
  .flyer--front .brand-name{left:0;width:100%;text-align:center;top:592px}

  .cta{position:absolute;left:0;top:651px;width:100%;height:38px;background:var(--navy);
       font:700 16px/40px "Josefin Sans",sans-serif;letter-spacing:1.6px;color:var(--sky);text-align:center}
  .contact{position:absolute;left:0;top:689px;width:100%;height:75px;background:var(--sky);
           font:400 15px/1 "Barlow Condensed",sans-serif;color:#fff;text-align:center;padding-top:15px}
  .contact__row{display:flex;justify-content:center;align-items:center;gap:14px;margin-bottom:7px}
  .contact__item{display:inline-flex;align-items:center;gap:4px}
  .contact svg{width:13px;height:13px;fill:var(--navy)}

  .services-head{position:absolute;left:0;top:0;width:100%;height:112px;background:var(--navy);
                 text-align:center;font-size:30px;line-height:112px}
  .services-head__our{font:italic 300 30px "Barlow Condensed",sans-serif;color:#fff}
  .services-head__title{font:700 28px "Josefin Sans",sans-serif;color:var(--sky);letter-spacing:1px}
  .service-grid{position:absolute;left:10px;top:126px;width:362px;display:grid;grid-template-columns:181px 181px;grid-auto-rows:128px}
  .service-photo{width:100%;height:100%}
  .service-label{position:relative;display:flex;align-items:center;justify-content:center;text-align:center;
                 font:500 16px/1.1 "Barlow Condensed",sans-serif;color:var(--text-dark);padding:0 18px}
  .service-label::before,.service-label::after{content:"";position:absolute;top:0;height:100%}
  .service-label--bar-right::before{right:5px;width:8px;background:var(--sky)}
  .service-label--bar-right::after{right:0;width:5px;background:var(--navy)}
  .service-label--bar-left::before{left:5px;width:8px;background:var(--sky)}
  .service-label--bar-left::after{left:0;width:5px;background:var(--navy)}

  .back-brand{position:absolute;left:30px;top:663px;display:flex;align-items:center;gap:14px}
  .back-brand__mark{width:54px;height:54px;border-radius:50%;border:3px solid var(--sky)}
  .back-brand .brand-name{position:static;font-size:26px}
  .back-footer{position:absolute;left:0;bottom:0;width:100%;height:22px;background:var(--sky)}
</style>
</head>
<body>
<main class="canvas">

  <section class="flyer flyer--front">
    <svg class="front-art" width="382" height="650" viewBox="0 0 382 650">
      <defs>
        <linearGradient id="photoTone" x1="0" y1="0" x2="0.25" y2="1">
          <stop offset="0" stop-color="#ffffff"/>
          <stop offset="0.22" stop-color="#f4f5f7"/>
          <stop offset="0.38" stop-color="#dcdfe5"/>
          <stop offset="0.55" stop-color="#c99b7d"/>
          <stop offset="1" stop-color="#9c6d50"/>
        </linearGradient>
        <clipPath id="heroClip">
          <rect x="0" y="0" width="382" height="290"/>
          <circle cx="190" cy="290" r="225"/>
        </clipPath>
      </defs>
      <circle cx="250" cy="295" r="240" fill="none" stroke="var(--navy)" stroke-width="5"/>
      <circle cx="190" cy="290" r="229" fill="var(--sky)"/>
      <rect x="0" y="0" width="382" height="650" fill="url(#photoTone)" clip-path="url(#heroClip)" role="img" aria-label="Foto: entspannte Frau bei einer Rückenmassage, Hände auf der Schulter"/>
      <path d="M86 0 A105 27 0 0 0 296 0 Z" fill="var(--sky)"/>
      <circle cx="192" cy="533" r="50" fill="var(--paper)"/>
      <circle cx="192" cy="533" r="42" fill="none" stroke="var(--sky)" stroke-width="4"/>
    </svg>
    <div class="tagline tagline__lead">Live at your</div>
    <div class="tagline tagline__main">PHYSICAL BEST</div>
    <div class="brand-name">LEIBESWERKSTATT</div>
    <div class="cta">BOOK YOUR APPOINTMENT</div>
    <div class="contact">
      <div class="contact__row">
        <span class="contact__item"><svg viewBox="0 0 24 24"><path d="M6.6 10.8a15 15 0 0 0 6.6 6.6l2.2-2.2a1 1 0 0 1 1-.25 11.4 11.4 0 0 0 3.6.57 1 1 0 0 1 1 1V20a1 1 0 0 1-1 1A17 17 0 0 1 3 4a1 1 0 0 1 1-1h3.5a1 1 0 0 1 1 1c0 1.25.2 2.450 .57 3.57a1 1 0 0 1-.25 1z"/></svg>03581 7140258</span>
        <span class="contact__item"><svg viewBox="0 0 24 24"><path d="M12 2a10 10 0 1 0 0 20 10 10 0 0 0 0-20zm6.9 6h-3a15.6 15.6 0 0 0-1.4-3.6A8 8 0 0 1 18.9 8zM12 4a14 14 0 0 1 1.9 4h-3.8A14 14 0 0 1 12 4zM4.3 14a8 8 0 0 1 0-4h3.4a16 16 0 0 0 0 4zm.8 2h3a15.6 15.6 0 0 0 1.4 3.6A8 8 0 0 1 5.1 16zm3-8h-3a8 8 0 0 1 4.3-3.6A15.6 15.6 0 0 0 8.1 8zM12 20a14 14 0 0 1-1.9-4h3.8A14 14 0 0 1 12 20zm2.3-6H9.7a14.7 14.7 0 0 1 0-4h4.6a14.7 14.7 0 0 1 0 4zm.3 5.6a15.6 15.6 0 0 0 1.4-3.6h3a8 8 0 0 1-4.4 3.6zM16.3 14a16 16 0 0 0 0-4h3.4a8 8 0 0 1 0 4z"/></svg>Leibeswerkstatt-beispielort.de</span>
      </div>
      <div class="contact__row">
        <span class="contact__item"><svg viewBox="0 0 24 24"><path d="M12 2a7 7 0 0 0-7 7c0 5.2 7 13 7 13s7-7.8 7-13a7 7 0 0 0-7-7zm0 9.5A2.5 2.5 0 1 1 12 6.5a2.5 2.5 0 0 1 0 5z"/></svg>Lindenweg 17, 07391 Beispielort</span>
      </div>
    </div>
  </section>

  <section class="flyer flyer--back">
    <header class="services-head" role="img" aria-label="Kopfbereich mit abgedunkeltem Foto eines Aromadiffusers"><span class="services-head__our">Our </span><span class="services-head__title">SERVICES</span></header>
    <div class="service-grid">
      <svg class="service-photo" role="img" aria-label="Foto: Therapeut behandelt die Schulter eines liegenden Mannes"><defs><linearGradient id="p1" x1="0" y1="0" x2="1" y2="1"><stop offset="0" stop-color="#e6e2de"/><stop offset=".5" stop-color="#d0a58a"/><stop offset="1" stop-color="#efeeec"/></linearGradient></defs><rect width="100%" height="100%" fill="url(#p1)"/></svg>
      <div class="service-label service-label--bar-right">Manuelle Therapie</div>
      <div class="service-label service-label--bar-left">Manuelle Lymphatic<br>Drainage</div>
      <svg class="service-photo" role="img" aria-label="Foto: Lymphdrainage am Bein"><defs><linearGradient id="p2" x1="0" y1="0" x2="1" y2="1"><stop offset="0" stop-color="#ede9e6"/><stop offset=".6" stop-color="#e0b8a2"/><stop offset="1" stop-color="#d6a892"/></linearGradient></defs><rect width="100%" height="100%" fill="url(#p2)"/></svg>
      <svg class="service-photo" role="img" aria-label="Foto: Hände massieren einen Rücken"><defs><linearGradient id="p3" x1="0" y1="0" x2="1" y2="1"><stop offset="0" stop-color="#6f7c8c"/><stop offset=".5" stop-color="#c9957a"/><stop offset="1" stop-color="#6e4a3a"/></linearGradient></defs><rect width="100%" height="100%" fill="url(#p3)"/></svg>
      <div class="service-label service-label--bar-right">Physiotherapie</div>
      <div class="service-label service-label--bar-left">Sektoraler Heilpraktiker<br>Physiotherapie</div>
      <svg class="service-photo" role="img" aria-label="Foto: Kinesio-Tape wird an der Schulter angelegt"><defs><linearGradient id="p4" x1="0" y1="0" x2="1" y2="1"><stop offset="0" stop-color="#a77a62"/><stop offset=".5" stop-color="#c49a82"/><stop offset="1" stop-color="#8d8d8f"/></linearGradient></defs><rect width="100%" height="100%" fill="url(#p4)"/></svg>
    </div>
    <div class="back-brand">
      <span class="back-brand__mark"></span>
      <span class="brand-name">LEIBESWERKSTATT</span>
    </div>
    <div class="back-footer"></div>
  </section>

</main>
</body>
</html>
```